Business Card Design for Consulting Company

I require a Business Card design for my Consulting company. <br/><br/>My company name is: Marcel Pruett Consulting Inc.<br/>My website is: www.marcelpruettconsulting.example<br/><br/>My company focuses on management and software development for the Tallyvane CRM platform (www.tallyvane.example)<br/><br/>I have a logo already designed...see attached.
Updates

Also Include my Name and Title: Marcel K.T. Pruett President

Target Market(s)

Tallyvane Customers

Contact Information for Business Card

Only include my LOGO (provided)
My Name: Marcel KT Pruett
My Title: President
My Company Name: Marcel Pruett Consulting Inc.
My Website: www.marcelpruettconsulting.example
My Email: marcel.pruett.consulting@mailbox.example

NO PHONE NUMBER
NO ADDRESS

Font styles to use
Serif
Sans Serif
Other font styles liked:
• see my website: www.marcelpruettconsulting.example

Colors

Designer to choose colors to be used in the design.

Requirements
Must have
• Must include my Orange
• Include my name (Marcel K.T. Pruett), title (President) company name, website and email
• It should also have a tag line like: Tallyvane Consulting
• I'm flexible with the tag line
Should not have
• Don't include my phone number or address

```html
<!DOCTYPE html>
<html lang="en">
<head>
<meta charset="utf-8">
<title>Marcel Pruett Consulting Inc. – Business Card</title>
<link rel="stylesheet" href="https://fonts.googleapis.com/css2?family=Roboto:wght@400;700;900&family=Ubuntu:wght@400;500;700&display=swap">
<style>
  :root {
    --backdrop: #3a3a3a;
    --card: #2b2b2b;
    --orange: #ff8a00;
    --white: #f4f4f4;
    --rule: #8a8a8a;
  }
  * { margin: 0; padding: 0; box-sizing: border-box; }
  html, body { width: 1200px; height: 901px; overflow: hidden; }
  body {
    background: var(--backdrop);
    display: flex;
    flex-direction: column;
    align-items: center;
    justify-content: center;
    gap: 56px;
    font-family: "Roboto", Arial, sans-serif;
  }
  .card {
    position: relative;
    width: 640px;
    height: 366px;
    background: var(--card);
    box-shadow: 0 10px 24px rgba(0,0,0,.35);
    overflow: hidden;
  }

  /* Front */
  .card-front {
    display: flex;
    align-items: center;
    justify-content: center;
    gap: 16px;
  }
  .brand-square {
    width: 26px;
    height: 26px;
    background: var(--orange);
  }
  .brand-name {
    font-family: "Ubuntu", Arial, sans-serif;
    font-weight: 700;
    font-size: 52px;
    color: var(--orange);
    letter-spacing: -0.5px;
  }

  /* Back */
  .card-back { display: flex; align-items: center; }
  .identity {
    width: 300px;
    display: flex;
    flex-direction: column;
    align-items: center;
    gap: 12px;
    padding-left: 24px;
    margin-top: -24px;
  }
  .identity .brand-name { font-size: 34px; }
  .company-name {
    font-weight: 700;
    font-size: 15px;
    color: var(--white);
    text-transform: uppercase;
    letter-spacing: .2px;
    white-space: nowrap;
  }
  .divider {
    width: 1px;
    height: 130px;
    background: var(--rule);
    margin: -24px 20px 0 8px;
  }
  .contact { margin-top: -24px; }
  .person-name {
    font-family: "Ubuntu", Arial, sans-serif;
    font-weight: 700;
    font-size: 24px;
    color: var(--orange);
    line-height: 1.05;
  }
  .person-title {
    font-family: "Ubuntu", Arial, sans-serif;
    font-size: 16px;
    color: var(--white);
    margin-bottom: 12px;
  }
  .tagline {
    font-family: "Ubuntu", Arial, sans-serif;
    font-size: 15px;
    color: var(--orange);
    letter-spacing: .6px;
    margin-bottom: 10px;
  }
  .contact-line {
    display: flex;
    align-items: center;
    gap: 8px;
    font-size: 14.5px;
    color: var(--white);
    line-height: 1.45;
    white-space: nowrap;
  }
  .contact-line svg { flex: none; }
  .accent-band {
    position: absolute;
    left: 0; right: 0; bottom: 0;
    height: 11px;
    background: var(--orange);
  }
</style>
</head>
<body>

  <section class="card card-front" aria-label="Card front">
    <span class="brand-square"></span>
    <span class="brand-name">Marcel Pruett</span>
  </section>

  <section class="card card-back" aria-label="Card back">
    <div class="identity">
      <span class="brand-name">Marcel Pruett</span>
      <span class="company-name">Marcel Pruett Consulting Inc</span>
    </div>
    <div class="divider"></div>
    <div class="contact">
      <p class="person-name">Marcel KT Pruett</p>
      <p class="person-title">President</p>
      <p class="tagline">Tallyvane Consulting</p>
      <p class="contact-line">
        <svg width="13" height="13" viewBox="0 0 14 14" aria-hidden="true">
          <circle cx="7" cy="7" r="6" fill="none" stroke="#ff8a00" stroke-width="1.6"/>
          <ellipse cx="7" cy="7" rx="2.6" ry="6" fill="none" stroke="#ff8a00" stroke-width="1.2"/>
          <line x1="1" y1="7" x2="13" y2="7" stroke="#ff8a00" stroke-width="1.2"/>
        </svg>
        www.marcelpruettconsulting.example
      </p>
      <p class="contact-line">
        <svg width="13" height="10" viewBox="0 0 14 10" aria-hidden="true">
          <rect x="0" y="0" width="14" height="10" fill="#ff8a00"/>
          <polyline points="0.5,0.5 7,5.5 13.5,0.5" fill="none" stroke="#2b2b2b" stroke-width="1.2"/>
        </svg>
        marcel.pruett.consulting@mailbox.example
      </p>
    </div>
    <div class="accent-band"></div>
  </section>

</body>
</html>
```